Looking for business card/letterhead/email signature

Take existing logo and create full design suite of collateral

Contact Information for Business Card

Use mock details that can be edited by us

Font styles to use
Sans Serif

```html
<!DOCTYPE html>
<html lang="en">
<head>
<meta charset="utf-8">
<title>Norwick Digital – Business Card</title>
<link rel="stylesheet" href="https://fonts.googleapis.com/css2?family=Open+Sans:wght@400;600;700;800&display=swap">
<style>
  :root {
    --navy: #0d4f9c;
    --sky: #2ea7e6;
    --white: #ffffff;
    --lime: #c9de2f;
    --stage: #2b2e33;
  }
  * { box-sizing: border-box; margin: 0; padding: 0; }
  html, body { width: 1200px; height: 900px; overflow: hidden; }
  body {
    background: var(--stage);
    font-family: "Open Sans", Arial, sans-serif;
    display: flex;
    flex-direction: column;
    align-items: center;
    justify-content: center;
    gap: 60px;
  }
  .card {
    position: relative;
    width: 560px;
    height: 320px;
    border-radius: 20px;
    overflow: hidden;
  }
  .card-front { background: var(--white); }
  .card-front .wave { position: absolute; inset: 0; }
  .holder { position: absolute; left: 36px; top: 38px; color: var(--white); }
  .holder-name { font-size: 26px; font-weight: 700; letter-spacing: 0.2px; line-height: 1.2; }
  .holder-role { font-size: 13px; margin-top: 2px; opacity: 0.9; }
  .address {
    position: absolute; left: 36px; top: 112px;
    color: var(--white); font-size: 13px; line-height: 1.45;
    display: flex; gap: 8px;
  }
  .brand { position: absolute; display: flex; align-items: center; gap: 10px; }
  .brand-name { font-weight: 800; font-size: 40px; letter-spacing: -1px; line-height: 1; }
  .brand-sub { display: block; font-weight: 400; font-size: 11px; letter-spacing: 4px; margin-top: 2px; }
  .brand-dot { width: 14px; height: 14px; border-radius: 50%; background: var(--sky); }
  .card-front .brand { right: 40px; top: 72px; color: var(--navy); }
  .contacts {
    position: absolute; right: 34px; bottom: 22px;
    color: var(--white); font-size: 15px; line-height: 1.6;
    list-style: none; text-align: right;
  }
  .contacts li { display: flex; align-items: center; justify-content: flex-end; gap: 8px; }
  .icon { width: 13px; height: 13px; flex: none; }
  .card-back { background: var(--navy); }
  .world-map {
    position: absolute; left: 70px; top: 20px; width: 430px; height: 260px;
    border-radius: 40%;
    background: radial-gradient(ellipse at center, rgba(255,255,255,0.10), rgba(255,255,255,0) 70%);
  }
  .card-back .brand { left: 50%; top: 104px; transform: translateX(-50%); color: var(--white); }
  .back-url {
    position: absolute; left: 0; right: 0; bottom: 86px;
    text-align: center; color: var(--white); font-size: 15px;
  }
</style>
</head>
<body>
  <section class="card card-front">
    <svg class="wave" viewBox="0 0 560 320" preserveAspectRatio="none" aria-hidden="true">
      <path d="M0,0 L246,0 C296,10 312,116 356,164 C398,204 476,204 560,204 L560,320 L0,320 Z" fill="#2ea7e6"/>
      <path d="M0,0 L232,0 C282,12 298,126 344,174 C388,214 472,214 560,214 L560,320 L0,320 Z" fill="#0d4f9c"/>
    </svg>
    <div class="holder">
      <div class="holder-name">Daniel Reyes</div>
      <div class="holder-role">Owner</div>
    </div>
    <div class="address">
      <svg class="icon" viewBox="0 0 12 16" aria-hidden="true"><path d="M6 0a6 6 0 0 0-6 6c0 4.5 6 10 6 10s6-5.5 6-10a6 6 0 0 0-6-6zm0 8.5a2.5 2.5 0 1 1 0-5 2.5 2.5 0 0 1 0 5z" fill="#c9de2f"/></svg>
      <span>18 Maple Crest Rd. Kanata,<br>ON K2T0A4</span>
    </div>
    <div class="brand">
      <span class="brand-dot"></span>
      <div class="brand-name">norwick<span class="brand-sub">DIGITAL</span></div>
    </div>
    <ul class="contacts">
      <li>+1 555 014 3381
        <svg class="icon" viewBox="0 0 16 16" aria-hidden="true"><path d="M3 1l3 3-2 2c1 2 3 4 5 5l2-2 3 3-2 3C6 15 1 10 1 3z" fill="#c9de2f"/></svg></li>
      <li>hello@norwickdigital.com
        <svg class="icon" viewBox="0 0 16 12" aria-hidden="true"><rect x="0" y="0" width="16" height="12" rx="1" fill="#c9de2f"/><path d="M0 0l8 6 8-6" stroke="#0d4f9c" stroke-width="1.5" fill="none"/></svg></li>
      <li>www.norwickdigital.com
        <svg class="icon" viewBox="0 0 16 16" aria-hidden="true"><circle cx="8" cy="8" r="7" fill="#c9de2f"/><path d="M1 8h14M8 1v14M3 4h10M3 12h10" stroke="#0d4f9c" stroke-width="1" fill="none"/></svg></li>
    </ul>
  </section>

  <section class="card card-back">
    <div class="world-map" role="img" aria-label="Faint world map backdrop"></div>
    <div class="brand">
      <span class="brand-dot"></span>
      <div class="brand-name">norwick<span class="brand-sub">DIGITAL</span></div>
    </div>
    <div class="back-url">www.norwickdigital.com</div>
  </section>
</body>
</html>
```